Brochure for International and Domestic Festival & Music Student Tour Company

We need a brochure for our Festival and Music Student Tour Company. Brochure needs to communicate clearly what we offer. It should be visually exciting and inspirational. We want to see our brand colors incorporated as well as the swoosh (I will provide image) we use on our other marketing materials. Think outside the box, we don't want a standard template. This needs to stand out and make people want to read it. Imagery is important. I have provided the content in a word document as well as images and logos. Brightwater Voyage Tours is the main logo but we also need to include the Halvik Tours logo (smaller) and the Family of Logos should be with the address. All these will be provided to you.

Target Market(s)

Music Directors - Middle School, High School, and College

Industry/Entity Type

Tourism

Font styles to use
Serif
Sans Serif

Requirements
Must have
• Our logos

```html
<!DOCTYPE html>
<html lang="en">
<head>
<meta charset="utf-8">
<title>Brightwater Voyage Tours – 2019 Festival Brochure</title>
<link rel="stylesheet" href="https://fonts.googleapis.com/css2?family=Open+Sans:wght@300;400;600;700;800&display=swap">
<style>
  :root{
    --stage:#e4e5e7;
    --blue:#2d97d9;
    --red:#c8232f;
    --navy:#3b3f8f;
    --white:#ffffff;
    --ink:#1f3f7a;
    --sky-top:#5677ad;
    --sky-warm:#d8a468;
    --stone:#b4875a;
  }
  *{box-sizing:border-box;margin:0;padding:0}
  html,body{width:1200px;height:824px;overflow:hidden;background:var(--stage);font-family:"Open Sans",sans-serif}
  .spread{position:absolute;left:80px;top:44px;width:1040px;height:736px;display:flex;box-shadow:0 6px 24px rgba(0,0,0,.18)}
  .page{position:relative;width:520px;height:736px;overflow:hidden;background:var(--blue)}
  .photo{position:absolute;left:0;top:0;width:520px}
  .back-cover .photo{height:620px;background:linear-gradient(180deg,var(--sky-top) 0%,#8ea3c4 28%,var(--sky-warm) 50%,var(--stone) 72%,#a67a52 100%)}
  .front-cover .photo{height:470px;background:linear-gradient(180deg,#6a9bd3 0%,#a9c7e6 35%,#8d9aae 62%,#5e9a84 80%,#708a9e 100%)}
  .swoosh{position:absolute;left:0;top:0;width:520px;height:736px}

  /* back cover */
  .partner-badges{position:absolute;left:22px;top:468px;display:flex;gap:10px;align-items:center}
  .badge{height:38px;border-radius:6px;background:rgba(40,40,50,.45)}
  .badge--wide{width:110px}
  .badge--mid{width:80px}
  .badge-halvik{height:38px;padding:0 12px;border-radius:6px;background:rgba(40,40,50,.45);display:flex;align-items:center;gap:6px;color:var(--white);font-weight:700;font-size:12px}
  .badge-halvik .dot{width:12px;height:12px;background:var(--red);border-radius:50%}

  .contact{position:absolute;left:256px;top:606px;color:var(--white);font-size:11.5px;white-space:nowrap}
  .contact h3{font-size:13px;font-weight:700;margin-bottom:6px}
  .contact-row{display:flex;align-items:center;gap:6px;margin-bottom:6px}
  .contact-row svg{width:13px;height:13px;flex:none}
  .social{display:inline-flex;gap:4px;margin-left:2px}
  .social span{width:11px;height:11px;border-radius:50%;background:var(--white)}
  .visit{display:flex;align-items:center;gap:8px;margin-top:4px}
  .visit-pill{background:var(--white);color:var(--blue);font-weight:700;font-size:12px;padding:3px 14px;border-radius:12px}
  .email{position:absolute;left:326px;top:584px;display:flex;align-items:center;gap:6px;color:var(--white);font-size:11.5px;white-space:nowrap}
  .email svg{width:13px;height:13px;flex:none}

  .brand{display:flex;align-items:center;gap:7px;color:var(--ink);font-weight:800;font-size:15px;line-height:1.05}
  .brand .mark{width:16px;height:16px;border-radius:50%;background:var(--red);flex:none}
  .back-cover .brand{position:absolute;left:24px;top:618px}
  .front-cover .brand{position:absolute;right:22px;top:18px}

  /* front cover */
  .headline{position:absolute;left:38px;top:492px;color:var(--white)}
  .headline h1{font-size:33px;font-weight:800;letter-spacing:.5px;line-height:1.05}
  .headline h2{font-size:29px;font-weight:300;letter-spacing:1px;line-height:1.1}
  .headline .rule{width:62px;height:5px;border-radius:3px;background:var(--white);margin:16px 0 12px}
  .headline p{width:420px;font-size:10.5px;line-height:1.45}
  .web-tab{position:absolute;right:0;top:300px;width:28px;height:190px;background:var(--red);display:flex;align-items:center;justify-content:center}
  .web-tab span{transform:rotate(-90deg);white-space:nowrap;color:var(--white);font-size:11px;font-weight:600;letter-spacing:.3px}
</style>
</head>
<body>
<main class="spread">

  <section class="page back-cover">
    <div class="photo" role="img" aria-label="Photograph of the Colosseum in Rome under a golden evening sky"></div>
    <svg class="swoosh" viewBox="0 0 520 736" aria-hidden="true">
      <path fill="var(--red)" d="M0 575 C180 560 340 470 520 415 L520 736 L0 736 Z"/>
      <path fill="var(--white)" d="M0 587 C180 572 340 482 520 427 L520 736 L0 736 Z"/>
      <path fill="var(--navy)" d="M0 712 C220 690 370 478 520 437 L520 736 L0 736 Z"/>
      <path fill="var(--blue)" d="M0 724 C220 702 370 490 520 447 L520 736 L0 736 Z"/>
    </svg>

    <div class="partner-badges">
      <div class="badge badge--wide"></div>
      <div class="badge badge--mid"></div>
      <div class="badge-halvik"><span class="dot"></span>Halvik Tours</div>
    </div>

    <div class="email">
      <svg viewBox="0 0 14 14"><circle cx="7" cy="7" r="7" fill="var(--red)"/><rect x="3.5" y="4.5" width="7" height="5" fill="none" stroke="#fff" stroke-width="1"/><path d="M3.5 4.5 L7 7.3 L10.5 4.5" fill="none" stroke="#fff" stroke-width="1"/></svg>
      info@brightwatervoyage.com
    </div>

    <div class="contact">
      <h3>Contact Us:</h3>
      <div class="contact-row">
        <svg viewBox="0 0 14 14"><circle cx="7" cy="7" r="7" fill="var(--red)"/><path d="M4.6 3.6c.4-.3.8-.2 1 .2l.6 1.1c.2.3.1.6-.2.8l-.4.3c.3.8 1 1.5 1.8 1.9l.3-.4c.2-.3.6-.4.9-.2l1.1.6c.4.2.5.6.2 1l-.5.6c-.4.4-1 .5-1.6.2-1.7-.8-3-2.1-3.7-3.8-.2-.6-.1-1.200.3-1.6z" fill="#fff"/></svg>
        555-014-2290
      </div>
      <div class="contact-row">Follow us: <span class="social"><span></span><span></span><span></span></span></div>
      <div class="visit"><span class="visit-pill">Visit On:</span>www.brightwatervoyage.com</div>
    </div>

    <div class="brand"><span class="mark"></span>Brightwater Voyage<br>Tours</div>
  </section>

  <section class="page front-cover">
    <div class="photo" role="img" aria-label="Photograph of the Statue of Liberty in front of the New York City skyline"></div>
    <svg class="swoosh" viewBox="0 0 520 736" aria-hidden="true">
      <path fill="var(--red)" d="M0 430 C180 470 340 330 520 255 L520 736 L0 736 Z"/>
      <path fill="var(--white)" d="M0 441 C180 481 340 341 520 266 L520 736 L0 736 Z"/>
      <path fill="var(--navy)" d="M0 451 C180 491 340 351 520 276 L520 736 L0 736 Z"/>
      <path fill="var(--blue)" d="M0 460 C180 500 340 360 520 285 L520 736 L0 736 Z"/>
    </svg>

    <div class="brand"><span class="mark"></span>Brightwater Voyage<br>Tours</div>

    <div class="headline">
      <h1>2019 FESTIVAL DATES</h1>
      <h2>NOW AVAILABLE!</h2>
      <div class="rule"></div>
      <p>Founded in 1989, Brightwater Voyage Tours &amp; Music Festivals is distinguished by a strong connection with the educational community. Successful music educators have played prominent roles throughout the company's history.</p>
    </div>

    <div class="web-tab"><span>www.brightwatervoyage.com</span></div>
  </section>

</main>
</body>
</html>
```